Quarrytide Hosting - Direct Mailer / Flyer

We are excited to announce the launch of our new company, Quarrytide Hosting, a premier cohosting facility and data center dedicated to Cryptocurrency Miners. Our website, https://quarrytidehosting.example, provides detailed information about our offerings and showcases the innovative design schemes for the entire project.

Quarrytide Hosting stands out in the industry by offering both GPU Hosting and ASIC Hosting services in our state-of-the-art facility, equipped with an impressive 17 Megawatts of available power. What sets us apart is our unique billing system based on actual metered power usage. We charge $0.08 for ASIC miners and $0.09 for GPU miners, ensuring cost-effectiveness and transparency for our clients.

Our commitment to excellence is evident in our use of cutting-edge technology, top-notch facilities, and strategic partnerships. These elements come together to deliver exceptional solutions tailored for real-world applications in the cryptocurrency space.

As part of our promotional efforts, we are developing a direct mailer/flyer to introduce Quarrytide Hosting to a wider audience. This promotional material will also serve as a handout at events, to potential customers, and more. We welcome creative ideas and suggestions to maximize the versatility of this design and reach diverse target audiences effectively.

For a comprehensive overview of our services and to explore our design concepts, please visit https://quarrytidehosting.example. Quarrytide Hosting is poised to revolutionize the mining industry, and we look forward to partnering with you for success in the digital currency era.

```html
<!DOCTYPE html>
<html lang="en">
<head>
<meta charset="utf-8">
<title>Quarrytide Hosting – Flyer</title>
<link href="https://fonts.googleapis.com/css2?family=Bebas+Neue&family=Montserrat:wght@400;500;600;700;800&display=swap" rel="stylesheet">
<style>
  :root {
    --canvas: #eef0f5;
    --royal: #3348f0;
    --royal-deep: #2a3bd6;
    --ink: #111111;
    --night: #1b1813;
    --night-2: #2c261a;
    --sun: #f1e14a;
    --paper: #f4f5fd;
    --paper-blue: #cdd3fa;
    --lilac-card: #cdd2fa;
    --mint-card: #d2e8df;
    --gpu-text: #3a4ee0;
    --asic-text: #1f8a2e;
    --money: #1e8a1e;
  }
  * { box-sizing: border-box; margin: 0; padding: 0; }
  html, body { width: 1050px; height: 1200px; overflow: hidden; background: var(--canvas); }
  body { font-family: "Montserrat", sans-serif; position: relative; }

  .sheet {
    position: absolute; top: 217px; width: 495px; height: 766px; overflow: hidden;
    background: linear-gradient(180deg, var(--paper) 0%, #e3e6fc 55%, var(--paper-blue) 100%);
    box-shadow: 0 4px 18px rgba(20, 30, 80, .18);
  }
  .sheet--front { left: 20px; }
  .sheet--back { left: 535px; }

  /* front */
  .front-shapes { position: absolute; inset: 0; }
  .brand { position: absolute; display: flex; align-items: center; gap: 9px; }
  .brand__mark { width: 28px; height: 22px; background: var(--ink); }
  .brand__name { font-weight: 800; color: var(--ink); text-transform: uppercase; letter-spacing: .5px; }
  .sheet--front .brand { left: 30px; top: 30px; }
  .sheet--front .brand__name { font-size: 24px; }

  .hero-title {
    position: absolute; left: 25px; top: 178px;
    font-family: "Bebas Neue", sans-serif; font-size: 40px; line-height: 1.12; color: var(--sun);
  }
  .hero-sub {
    position: absolute; left: 25px; top: 288px; width: 300px;
    color: #fff; font-size: 16.5px; line-height: 1.27; font-weight: 500;
  }
  .intro {
    position: absolute; left: 25px; right: 25px; top: 420px;
    font-size: 10.6px; line-height: 1.42; text-align: justify; color: var(--ink);
  }
  .intro .power { color: var(--royal); font-weight: 700; }
  .intro .rate { color: var(--money); font-weight: 700; }
  .commitment {
    position: absolute; left: 25px; top: 532px; width: 210px;
    font-size: 10.6px; line-height: 1.42; color: var(--ink);
  }
  .illustration {
    position: absolute; left: 262px; top: 513px; width: 200px; height: 232px; border-radius: 14px;
    background: radial-gradient(ellipse at 55% 45%, #f2e46a 0%, #b9c1f7 55%, rgba(190,198,248,0) 80%);
  }
  .cta-band {
    position: absolute; left: 0; bottom: 0; width: 100%; height: 67px; background: var(--royal);
  }
  .cta {
    position: absolute; left: 132px; top: 710px; color: #fff;
  }
  .cta__kicker { font-size: 9.5px; font-weight: 500; letter-spacing: .3px; }
  .cta__line { font-size: 12.5px; font-weight: 700; color: var(--sun); line-height: 1.25; margin-top: 2px; }

  /* back */
  .photo {
    position: absolute; left: 0; top: 0; width: 100%; height: 270px;
    background: linear-gradient(180deg, #0b1028 0%, #1a2460 45%, #4b5ad8 78%, rgba(228,231,252,0) 100%);
  }
  .solutions-title {
    position: absolute; left: 0; right: 0; top: 286px; text-align: center;
    font-family: "Bebas Neue", sans-serif; font-size: 43px; line-height: 1.05; color: var(--royal);
  }
  .solutions-sub {
    position: absolute; left: 30px; right: 30px; top: 384px; text-align: center;
    font-size: 12px; line-height: 1.4; font-weight: 700; color: var(--ink);
  }
  .plan {
    position: absolute; top: 448px; width: 200px; height: 226px; border-radius: 10px; padding: 17px 14px 0 15px;
  }
  .plan--gpu { left: 38px; background: var(--lilac-card); color: var(--gpu-text); }
  .plan--asic { left: 264px; background: var(--mint-card); color: var(--asic-text); }
  .plan__title { font-size: 13px; font-weight: 700; margin-bottom: 10px; }
  .plan__text { font-size: 8.1px; line-height: 1.35; margin-bottom: 10px; }
  .plan__list { list-style: none; }
  .plan__list li {
    position: relative; padding-left: 12px; font-size: 8.1px; font-weight: 700; line-height: 1.3; margin-bottom: 10px;
  }
  .plan__list svg { position: absolute; left: 0; top: 1px; width: 7px; height: 7px; }

  .footer-band {
    position: absolute; left: 0; bottom: 0; width: 100%; height: 67px; background: var(--royal);
  }
  .sheet--back .brand { left: 122px; top: 712px; gap: 6px; }
  .sheet--back .brand__mark { width: 17px; height: 13px; }
  .sheet--back .brand__name { font-size: 13px; }
  .tagline {
    position: absolute; left: 122px; top: 737px; color: #fff; font-size: 7.6px; font-weight: 700; line-height: 1.3;
  }
  .contact {
    position: absolute; left: 353px; top: 706px; color: #fff; font-size: 7.6px; line-height: 1.3; font-weight: 500;
  }
  .contact dd { font-weight: 600; margin-bottom: 9px; }
</style>
</head>
<body>

<section class="sheet sheet--front" aria-label="Flyer front">
  <svg class="front-shapes" viewBox="0 0 495 766" width="495" height="766">
    <polygon points="410,0 495,0 495,40" fill="#dfe3fc"/>
    <polygon points="0,88 228,88 300,62 468,0 495,0 495,50 310,88 240,103 0,103" fill="var(--royal)"/>
    <g role="img" aria-label="Dark 3D render of a glowing mining cube on a circuit board">
      <defs>
        <linearGradient id="night" x1="0" y1="0" x2="1" y2="1">
          <stop offset="0" stop-color="#17140f"/>
          <stop offset="1" stop-color="#2e2819"/>
        </linearGradient>
      </defs>
      <polygon points="0,103 240,103 310,88 495,50 495,340 445,390 0,390" fill="url(#night)"/>
    </g>
  </svg>

  <div class="brand"><span class="brand__mark"></span><span class="brand__name">Quarrytide Hosting</span></div>

  <h1 class="hero-title">Transform Mining<br>with Cohosting</h1>
  <p class="hero-sub">Miners deserve the best - choose the hosting company that delivers excellence!</p>

  <p class="intro">Quarrytide Hosting stands out in the industry by offering both GPU Hosting and ASIC Hosting services in our state-of-the-art facility, equipped with an impressive <span class="power">17 Megawatts</span> of available power. What sets us apart is our unique billing system based on actual metered power usage. We charge <span class="rate">$0.08 for ASIC miners</span> and <span class="rate">$0.09</span> for <span class="rate">GPU miners</span>, ensuring cost-effectiveness and transparency for our clients.</p>

  <p class="commitment">Our commitment to excellence is evident in our use of cutting-edge technology, top-notch facilities, and strategic partnerships. These elements come together to deliver exceptional solutions tailored for real-world applications in the cryptocurrency space.</p>

  <div class="cta-band"></div>
  <div class="illustration" role="img" aria-label="Illustration of workers carrying gold coins and server stacks"></div>
  <div class="cta">
    <p class="cta__kicker">ARE YOU READY?</p>
    <p class="cta__line">Your Mining Success<br>Story Begins Here</p>
  </div>
</section>

<section class="sheet sheet--back" aria-label="Flyer back">
  <div class="photo" role="img" aria-label="Photo of hands holding a tablet projecting a glowing crypto coin hologram"></div>

  <h2 class="solutions-title">Solutions for every miner,<br>regardless of scale</h2>
  <p class="solutions-sub">Our solutions cater to cryptominers of all sizes, providing tailored options to meet diverse operational needs.</p>

  <article class="plan plan--gpu">
    <h3 class="plan__title">GPU Hosting</h3>
    <p class="plan__text">Benefit from GPU hosting at an affordable rate of $0.09 per kilowatt-hour, ensurin cost-effective operations for your mining needs on any algorithm.</p>
    <ul class="plan__list">
      <li><svg viewBox="0 0 10 10"><circle cx="5" cy="5" r="3.8" fill="none" stroke="currentColor" stroke-width="1.6"/></svg>One Time Setup Fee of $50 Per GPU Rig</li>
      <li><svg viewBox="0 0 10 10"><circle cx="5" cy="5" r="3.8" fill="none" stroke="currentColor" stroke-width="1.6"/></svg>All-In $0.09 Per Kilowatt-Hour, No Additional Fees</li>
      <li><svg viewBox="0 0 10 10"><circle cx="5" cy="5" r="3.8" fill="none" stroke="currentColor" stroke-width="1.6"/></svg>Remotely Monitor &amp; Access Your Equipment 24/7</li>
    </ul>
  </article>

  <article class="plan plan--asic">
    <h3 class="plan__title">ASIC Hosting</h3>
    <p class="plan__text">Access ASIC hosting at a competitive rate of $0.08 per kilowatt-hour, ensuring efficient and cost-effective operations for your large scale mining endeavors.</p>
    <ul class="plan__list">
      <li><svg viewBox="0 0 10 10"><circle cx="5" cy="5" r="3.8" fill="none" stroke="currentColor" stroke-width="1.6"/></svg>One Time Setup Fee of $50 Per ASIC Unit</li>
      <li><svg viewBox="0 0 10 10"><circle cx="5" cy="5" r="3.8" fill="none" stroke="currentColor" stroke-width="1.6"/></svg>All-In $0.08 Per Kilowatt-Hour, No Additional Fees</li>
      <li><svg viewBox="0 0 10 10"><circle cx="5" cy="5" r="3.8" fill="none" stroke="currentColor" stroke-width="1.6"/></svg>Remotely Monitor &amp; Access Your Equipment 24/7</li>
    </ul>
  </article>

  <div class="footer-band"></div>
  <div class="brand"><span class="brand__mark"></span><span class="brand__name">Quarrytide Hosting</span></div>
  <p class="tagline">METERED, RELIABLE, SECURE -<br>MINERS DESERVE THE BEST HOSTING.</p>
  <dl class="contact">
    <dt>Email us:</dt>
    <dd>hello@quarrytidehosting.example</dd>
    <dt>Web:</dt>
    <dd>www.quarrytidehosting.example</dd>
  </dl>
</section>

</body>
</html>
```